Design a modern, classy & professional business card for an online real estate agency, specializing in medium-luxury properties in Thailand and later in Singapore and UK.

Possible design ideas so far: (not essential)

- curved corner(s) to the card, white on front & turquoise on back or visa versa.

- front of card - clear and simple, company name in metallic grey/monochrome, logo graphic & company name on front in spot UV or embossed/debossed effect.

- back of card - large, close-cropped, 'ghost' patterns of the C-shaped curves of logo, or company name repeated on back of card in spot UV.

Target Market(s)

- young to middle-aged professionals mainly (but ideally should design should suit all)

- UK, US,EU,AUS & ASIAN mainly (but ideally should design should suit all countries)

Industry/Entity Type

Real Estate

Requirements
Must have
• THEME:
- Luxurious & Modern
- Clean & striking
- Unique & creative

INFO:
- Logo & company name on front
- Contact details on back:

Tobias Lindqvar
Managing Director

www.velmoraestates.example
www.velmoraestates-uk.example

Tel: 084-273-6190
email: tobias@velmoraestates.example

(contact details can be displayed in any order as suites design.)

Nice to have
• - curved corner(s) to the card, white on front & turquoise on back or visa versa.

Should not have
• - No generic images of properties, palm trees/coconut trees etc.

- No other other bold colors, except for main turquoise, grey, metallic white & black theme.

- No obvious business card templates

```html
<!DOCTYPE html>
<html lang="en">
<head>
<meta charset="utf-8">
<title>Velmora Estates — Business Card</title>
<link rel="stylesheet" href="https://fonts.googleapis.com/css2?family=Crimson+Pro:wght@400;600&display=swap">
<style>
  :root {
    --turquoise: #2cb8ae;
    --turquoise-deep: #22a69c;
    --paper: #f7f7f5;
    --grey-ink: #6e6e6e;
    --white-ink: #ffffff;
    --backdrop: #e4e4e2;
    --shadow: rgba(0, 0, 0, 0.18);
  }
  * { box-sizing: border-box; margin: 0; padding: 0; }
  html, body {
    width: 1200px;
    height: 801px;
    overflow: hidden;
    background: var(--backdrop);
    font-family: "Crimson Pro", Georgia, serif;
  }
  .stage {
    width: 1200px;
    height: 801px;
    display: flex;
    align-items: center;
    justify-content: center;
    gap: 60px;
  }
  .card {
    position: relative;
    width: 520px;
    height: 298px;
    border-radius: 6px;
    box-shadow: 0 10px 28px var(--shadow);
    overflow: hidden;
  }
  .brand {
    display: flex;
    align-items: center;
    gap: 10px;
  }
  .brand__square {
    background: var(--white-ink);
    flex: none;
  }
  .brand__name {
    font-weight: 400;
    line-height: 1;
    letter-spacing: 0.01em;
    white-space: nowrap;
  }

  /* Contact side */
  .card--contact {
    background: linear-gradient(160deg, var(--turquoise) 0%, var(--turquoise-deep) 100%);
    color: var(--white-ink);
  }
  .card--contact .brand {
    position: absolute;
    left: 34px;
    top: 124px;
  }
  .card--contact .brand__square {
    width: 34px;
    height: 34px;
  }
  .card--contact .brand__name {
    font-size: 23px;
  }
  .person {
    position: absolute;
    right: 34px;
    top: 34px;
    text-align: right;
  }
  .person__name {
    font-weight: 600;
    font-size: 23px;
    letter-spacing: 0.02em;
    white-space: nowrap;
  }
  .person__role {
    font-size: 13px;
    letter-spacing: 0.04em;
    margin-top: 2px;
  }
  .contact-list {
    position: absolute;
    left: 290px;
    top: 118px;
    list-style: none;
    font-size: 13px;
    line-height: 1.7;
    white-space: nowrap;
  }
  .contact-list li {
    display: flex;
    align-items: center;
    gap: 7px;
  }
  .contact-list svg { width: 11px; height: 11px; flex: none; }
  .web-list {
    position: absolute;
    left: 34px;
    bottom: 28px;
    list-style: none;
    font-size: 13px;
    line-height: 1.55;
    letter-spacing: 0.02em;
    white-space: nowrap;
  }

  /* Brand side */
  .card--brand {
    background: var(--paper);
    display: flex;
    align-items: center;
    justify-content: center;
  }
  .card--brand .brand { gap: 16px; }
  .card--brand .brand__square {
    width: 62px;
    height: 62px;
    background: var(--turquoise);
  }
  .card--brand .brand__name {
    color: var(--grey-ink);
    font-size: 44px;
  }
</style>
</head>
<body>
<main class="stage">
  <section class="card card--contact" aria-label="Contact side">
    <div class="brand">
      <span class="brand__square"></span>
      <span class="brand__name">Velmora Estates</span>
    </div>
    <div class="person">
      <p class="person__name">Tobias Lindqvar</p>
      <p class="person__role">Managing Director</p>
    </div>
    <ul class="contact-list">
      <li>
        <svg viewBox="0 0 12 12" aria-hidden="true"><rect width="12" height="12" rx="1" fill="#fff"/><path d="M3.2 2.5c.4-.3.9-.2 1.1.2l.6 1.1c.2.4.1.8-.2 1l-.4.3c.4.9 1 1.5 1.9 1.9l.3-.4c.2-.3.6-.4 1-.2l1.1.6c.4.2.5.7.2 1.1l-.5.6c-.4.4-1 .5-1.5.3C5.1 8.4 3.6 6.9 3 5.2c-.2-.5-.1-1.1.3-1.5z" fill="#2cb8ae"/></svg>
        084-273-6190
      </li>
      <li>
        <svg viewBox="0 0 12 12" aria-hidden="true"><rect width="12" height="12" rx="1" fill="#fff"/><rect x="2.2" y="3.5" width="7.6" height="5" fill="none" stroke="#2cb8ae" stroke-width="0.9"/><path d="M2.2 3.5 6 6.4l3.8-2.9" fill="none" stroke="#2cb8ae" stroke-width="0.9"/></svg>
        tobias@velmoraestates.example
      </li>
    </ul>
    <ul class="web-list">
      <li>www.velmoraestates.example</li>
      <li>www.velmoraestates-uk.example</li>
    </ul>
  </section>

  <section class="card card--brand" aria-label="Brand side">
    <div class="brand">
      <span class="brand__square"></span>
      <span class="brand__name">Velmora Estates</span>
    </div>
  </section>
</main>
</body>
</html>
```